BKA

Please send us some options for letterhead I attached our Logo. In addition to the Logo we need this information somewhere on the page

47 Fenbury Lane
Harlow Bay, VT 05921
555-481-7629

```html
<!DOCTYPE html>
<html lang="en">
<head>
<meta charset="utf-8">
<title>BKA Letterhead</title>
<link href="https://fonts.googleapis.com/css2?family=Open+Sans:wght@400;600;700&display=swap" rel="stylesheet">
<style>
  :root {
    --backdrop: #ececec;
    --paper: #ffffff;
    --ink: #3a2f2b;
    --brown: #3b2a25;
    --blue: #1f73b7;
    --sky: #d6e6f0;
    --stone: #d6d6d6;
    --rule: #8a8a8a;
  }
  * { margin: 0; padding: 0; box-sizing: border-box; }
  html, body {
    width: 900px; height: 1200px; overflow: hidden;
    background: var(--backdrop);
    font-family: "Open Sans", sans-serif;
    color: var(--ink);
  }
  .letterhead {
    position: absolute; left: 136px; top: 187px;
    width: 628px; height: 826px;
    background: var(--paper);
    box-shadow: 0 6px 18px rgba(0,0,0,0.12);
    overflow: hidden;
  }
  .brand {
    position: absolute; left: 59px; top: 62px;
    display: flex; align-items: center; gap: 12px;
  }
  .brand-square { width: 34px; height: 34px; background: var(--brown); }
  .brand-name {
    font-size: 30px; font-weight: 700; letter-spacing: 2px; color: var(--brown);
  }
  .letter-body {
    position: absolute; left: 84px; top: 272px; width: 440px;
    font-size: 10.5px; line-height: 14px;
  }
  .letter-body p { margin-bottom: 13px; }
  .letter-body .salutation { margin-top: 26px; }
  .letter-body .date, .letter-body .matter { font-weight: 700; }
  .letter-body .order-number { display: inline-block; width: 32px; }
  .signature {
    position: absolute; left: 84px; top: 546px;
    width: 170px; height: 52px;
    background: linear-gradient(90deg, #f3f3f3, #e8e8e8);
    border-radius: 4px;
  }
  .corner-decoration {
    position: absolute; left: 422px; top: 512px;
    width: 206px; height: 266px;
  }
  .footer-contact {
    position: absolute; left: 0; right: 0; top: 786px;
    font-size: 10.5px; line-height: 14px; color: var(--ink);
    display: flex; justify-content: center; align-items: center; gap: 8px;
  }
  .footer-contact svg { width: 11px; height: 11px; fill: var(--blue); }
  .footer-contact .divider { color: var(--rule); }
  .band-dark { position: absolute; left: 0; top: 808px; width: 497px; height: 18px; background: var(--brown); }
  .band-blue { position: absolute; left: 503px; top: 808px; width: 125px; height: 18px; background: var(--blue); }
</style>
</head>
<body>
<div class="letterhead">
  <div class="brand">
    <div class="brand-square"></div>
    <div class="brand-name">BKA</div>
  </div>

  <div class="letter-body">
    <p class="date">28 June 2013</p>
    <p>[Insert Name and Address of Solicitor]</p>
    <p class="salutation">Dear Mr/Ms [Solicitor Name]</p>
    <p class="matter">[Insert Matter details]</p>
    <p>In this matter [Insert details of what happened]<br>[Insert who appeared for the Other Party]</p>
    <p>The following Orders were made;<br><span class="order-number">1.</span>[Insert Orders that were made]</p>
    <p>If I can assist you with anything further please do not hesitate to contact me.<br>I enclose a memorandum of fees for your attention.</p>
    <p>Yours faithfully</p>
  </div>

  <div class="signature" role="img" aria-label="Handwritten signature"></div>

  <svg class="corner-decoration" viewBox="0 0 206 266" role="img" aria-label="Large faint brand decoration in grey and light blue">
    <defs>
      <linearGradient id="cornerFade" x1="0" y1="0" x2="0" y2="1">
        <stop offset="0" stop-color="var(--stone)"/>
        <stop offset="1" stop-color="var(--sky)"/>
      </linearGradient>
    </defs>
    <rect x="0" y="0" width="206" height="266" fill="url(#cornerFade)" opacity="0.75"/>
  </svg>

  <div class="footer-contact">
    <svg viewBox="0 0 12 12" aria-hidden="true"><path d="M6 1 L11 6 H9.5 V11 H7 V8 H5 V11 H2.5 V6 H1 Z"/></svg>
    <span>47 Fenbury Lane , Harlow Bay, VT 05921</span>
    <span class="divider">|</span>
    <svg viewBox="0 0 12 12" aria-hidden="true"><path d="M2 3 Q6 0 10 3 L9 5 L7 4.5 V4 H5 V4.5 L3 5 Z M3 6 H9 L10 10 H2 Z"/></svg>
    <span>555-481-7629</span>
  </div>

  <div class="band-dark"></div>
  <div class="band-blue"></div>
</div>
</body>
</html>
```